Business card design needed

We need a business card design for a new micro business based in Melbourne (Australia). Our main service is cleaning and fixing Vertical Blinds as a cheaper alternative than buying new blinds. A smaller part of the business is fitting affordable & temporary alternatives to double glazed windows both for noise abatement and climate control and reduction in energy costs.
We could be dealing with commercial as well as residential customers so we need a quality look. The design needs to reflect our core business of vertical blinds cleaning & maintenance.

Target Market(s)

Not sure yet. These Business Cards are going to be used to test the market

Industry/Entity Type

Residential

Contact Information for Business Card

Morlena Tazwick. Vertical Blinds Cleaning, Maintenance & Temporary Window Insulation Solutions. Ph: 03 7142 5063. Mob: 0471 356 249.

```html
<!DOCTYPE html>
<html lang="en">
<head>
<meta charset="utf-8">
<title>Morlena Tazwick – Business Card</title>
<link rel="stylesheet" href="https://fonts.googleapis.com/css2?family=Roboto+Condensed:wght@300;400&family=Jost:wght@400&family=Tinos:wght@700&display=swap">
<style>
  :root {
    --page-bg: #e6e6e6;
    --card-slate: #2d343b;
    --card-ink: #1c2026;
    --accent-yellow: #f6c200;
    --accent-blue: #0b8fd8;
    --name-blue: #6fc0ef;
    --tagline-grey: #a2aab2;
    --rule-gold: #c9a21a;
    --rule-grey: #7d858d;
    --white: #ffffff;
  }
  * { margin: 0; padding: 0; box-sizing: border-box; }
  html, body {
    width: 1200px;
    height: 800px;
    overflow: hidden;
    background: var(--page-bg);
  }
  .canvas {
    position: relative;
    width: 1200px;
    height: 800px;
  }
  .card {
    position: absolute;
    left: 421px;
    top: 80px;
    width: 358px;
    height: 640px;
    border-radius: 18px;
    overflow: hidden;
    background: var(--card-slate);
  }
  .card__art {
    position: absolute;
    inset: 0;
  }
  .card__name {
    position: absolute;
    left: 0;
    right: 0;
    top: 128px;
    text-align: center;
    font-family: "Roboto Condensed", "Arial Narrow", sans-serif;
    font-weight: 400;
    font-size: 35px;
    letter-spacing: -0.3px;
    color: var(--name-blue);
    text-transform: uppercase;
  }
  .card__tagline {
    position: absolute;
    left: 0;
    right: 0;
    top: 224px;
    text-align: center;
    font-family: "Jost", "Futura", sans-serif;
    font-size: 21px;
    line-height: 33px;
    color: var(--tagline-grey);
  }
</style>
</head>
<body>
<main class="canvas">
  <section class="card" aria-label="Business card for Morlena Tazwick">
    <svg class="card__art" width="358" height="640" viewBox="0 0 358 640" aria-hidden="true">
      <defs>
        <linearGradient id="gold-rule" x1="0" x2="1" y1="0" y2="0">
          <stop offset="0" stop-color="var(--rule-gold)"/>
          <stop offset="0.8" stop-color="var(--rule-gold)"/>
          <stop offset="1" stop-color="var(--rule-gold)" stop-opacity="0"/>
        </linearGradient>
        <linearGradient id="grey-rule" x1="0" x2="1" y1="0" y2="0">
          <stop offset="0" stop-color="var(--rule-grey)" stop-opacity="0"/>
          <stop offset="0.25" stop-color="var(--rule-grey)"/>
          <stop offset="1" stop-color="var(--rule-grey)"/>
        </linearGradient>
      </defs>

      <!-- lower contact band -->
      <rect class="band-contact" x="0" y="390" width="358" height="250" fill="var(--card-ink)"/>

      <!-- top-left accent swoosh -->
      <path class="swoosh-top" d="M-20,70 L48,70 Q74,70 90,46 L128,-12"
            fill="none" stroke="var(--accent-yellow)" stroke-width="34" stroke-linejoin="round"/>

      <!-- rules around name -->
      <rect class="rule-gold" x="122" y="117" width="236" height="2" fill="url(#gold-rule)"/>
      <rect class="rule-grey" x="8" y="184" width="228" height="1.5" fill="url(#grey-rule)"/>

      <!-- bottom-right chevron layers -->
      <path class="chevron-yellow" d="M72,640 L188,446 Q206,418 234,432 L358,500 L358,640 Z" fill="var(--accent-yellow)"/>
      <path class="chevron-slate" d="M176,640 L266,524 Q284,500 310,514 L358,542 L358,640 Z" fill="var(--card-slate)"/>
      <path class="chevron-blue" d="M268,640 L312,578 Q324,562 342,572 L358,582 L358,640 Z" fill="var(--accent-blue)"/>

      <!-- phone icon -->
      <g class="icon-phone" transform="translate(38,548)">
        <path d="M-10,12 L-15,20 L-3,14 Z" fill="var(--white)"/>
        <circle r="16" fill="var(--white)"/>
        <path d="M-7,-6 Q-9,2 -3,8 Q3,13 9,9 L6,4 L2,6 Q-3,3 -3,-2 L0,-5 Z" fill="var(--card-ink)"/>
      </g>
      <!-- mobile icon -->
      <g class="icon-mobile" transform="translate(76,575)">
        <path d="M-10,12 L-15,20 L-3,14 Z" fill="var(--white)"/>
        <circle r="16" fill="var(--white)"/>
        <rect x="-9" y="-5" width="18" height="10" rx="1.5" fill="var(--card-ink)"/>
        <rect x="-2" y="-3" width="9" height="6" fill="var(--white)"/>
      </g>

      <!-- contact numbers -->
      <g font-family="Tinos, 'Times New Roman', serif" font-weight="700" font-size="15" fill="var(--white)">
        <text class="contact-phone" transform="translate(64,512) rotate(-52)">: 03 7142 5063</text>
        <text class="contact-mobile" transform="translate(100,546) rotate(-52)">: 0471 356 249</text>
      </g>
    </svg>

    <h1 class="card__name">Morlena Tazwick</h1>
    <p class="card__tagline">Vertical Cleaning,<br>Maintenance and<br>Temporary Insulation<br>Solutions for Windows.</p>
  </section>
</main>
</body>
</html>
```